Business Card - Professional Minimalist - Double sided

We appreciate minimalist logo/web/collateral designs that allow design to tell a story. We want to relay a professional image/approach but throwing in a splash of modern when we’re able so long as it’s not distracting. Think 75% classic corporate, 25% modern. Open to black or white design, not sure which might look the best.

Target Market(s)

Senior executives or related government affairs contacts within the agriculture, energy, and defense industries (i.e., potential clients) but located outside of Washington, DC. Most potential clients based in DC with be familiar with both of us and our shared history.

Industry/Entity Type

Consulting

Contact Information for Business Card

Name: Daniel R. Whitlock
Title: Co-Founder & Partner
Address: 418 Bramblewood Ave. SE | Suite 2716 | Washington, D.C. 20019
Phone: (202) 555-0187
Email: Daniel@HollerbyWhitlock.com

Font styles to use
Serif

Colors

Designer to choose only greyscale colors for use in the design.

Requirements
Must have
• Name: Daniel R. Whitlock
Phone: (202) 555-0187

```html
<!DOCTYPE html>
<html lang="en">
<head>
<meta charset="utf-8">
<title>Hollerby Whitlock Group — Business Card</title>
<link rel="stylesheet" href="https://fonts.googleapis.com/css2?family=Marcellus&family=Roboto:wght@400;700&display=swap">
<style>
  :root {
    --stage: #2b2b2c;
    --card: #1d1d1e;
    --card-edge: #262627;
    --ink: #b9b9b9;
    --ink-muted: #8c8c8c;
    --rule: #5a5a5a;
    --mark: #6e6e6e;
  }
  * { box-sizing: border-box; margin: 0; padding: 0; }
  html, body { width: 1200px; height: 900px; overflow: hidden; }
  body {
    background: var(--stage);
    font-family: "Roboto", Arial, sans-serif;
    color: var(--ink);
    display: flex;
    flex-direction: column;
    align-items: center;
    justify-content: center;
    gap: 60px;
  }
  .card {
    position: relative;
    width: 600px;
    height: 343px;
    background: var(--card);
    border: 1px solid var(--card-edge);
    box-shadow: 0 10px 30px rgba(0,0,0,.45);
  }
  .wordmark {
    display: flex;
    align-items: center;
    gap: 12px;
    color: var(--mark);
    font-family: "Marcellus", "Times New Roman", serif;
    font-weight: 400;
    text-transform: uppercase;
    letter-spacing: 0.1em;
    line-height: 1.25;
    white-space: nowrap;
  }
  .wordmark__square {
    width: 30px;
    height: 30px;
    background: var(--mark);
    flex: none;
  }
  /* Front */
  .card--front .wordmark {
    position: absolute;
    left: 32px;
    top: 142px;
    font-size: 13px;
    color: var(--ink-muted);
    gap: 10px;
  }
  .card--front .wordmark__square { width: 24px; height: 24px; background: var(--ink-muted); }
  .divider {
    position: absolute;
    left: 300px;
    top: 108px;
    width: 1px;
    height: 146px;
    background: var(--rule);
  }
  .contact {
    position: absolute;
    left: 318px;
    top: 108px;
    font-size: 14px;
    line-height: 1.42;
    color: var(--ink);
  }
  .contact__name {
    font-size: 17px;
    font-weight: 700;
    color: var(--ink-muted);
    margin-bottom: 2px;
  }
  .contact__line { display: flex; align-items: center; gap: 6px; white-space: nowrap; }
  .contact__line svg { width: 10px; height: 10px; flex: none; }
  /* Back */
  .card--back .wordmark {
    position: absolute;
    right: 40px;
    top: 138px;
    font-size: 24px;
  }
  .card--back .wordmark__square { width: 44px; height: 44px; }
</style>
</head>
<body>
  <section class="card card--back" aria-label="Card back">
    <div class="wordmark">
      <span class="wordmark__square"></span>
      <span class="wordmark__name">Hollerby Whitlock<br>Group</span>
    </div>
  </section>

  <section class="card card--front" aria-label="Card front">
    <div class="wordmark">
      <span class="wordmark__square"></span>
      <span class="wordmark__name">Hollerby Whitlock<br>Group</span>
    </div>
    <div class="divider"></div>
    <div class="contact">
      <p class="contact__name">Daniel R. Whitlock</p>
      <p>Co-Founder &amp; Partner</p>
      <p>418 Bramblewood Ave. SE</p>
      <p>Suite 2716 | Washington, D.C. 20019</p>
      <p class="contact__line">
        <svg viewBox="0 0 10 10" aria-hidden="true"><path d="M2 1 L4 1 L4.6 3 L3.4 3.8 Q4.4 5.8 6.2 6.6 L7 5.4 L9 6 L9 8 Q5 9.4 1 4 Q1 2 2 1Z" fill="var(--ink-muted)"/></svg>
        (202) 555-0187
      </p>
      <p class="contact__line">
        <svg viewBox="0 0 10 10" aria-hidden="true"><rect x="0.5" y="2" width="9" height="6.4" fill="var(--ink-muted)"/><path d="M0.8 2.3 L5 5.6 L9.2 2.3" stroke="var(--card)" stroke-width="0.9" fill="none"/></svg>
        Daniel@HollerbyWhitlock.com
      </p>
      <p class="contact__line">
        <svg viewBox="0 0 10 10" aria-hidden="true"><circle cx="5" cy="5" r="4.5" fill="var(--ink-muted)"/><path d="M0.5 5 H9.5 M5 0.5 Q2.4 5 5 9.5 M5 0.5 Q7.6 5 5 9.5" stroke="var(--card)" stroke-width="0.7" fill="none"/></svg>
        HollerbyWhitlock.com
      </p>
    </div>
  </section>
</body>
</html>
```